Corvelle vineyards

Wine label/logo that is old world witH a modern Maybe Latin/Hispanic twist. Nothing cartoonish or colorful.

This is a wine vineyard growing tempranillo, Malbec, cabarnet. I am looking for a wine label that incorporates the logo for Corvelle Vineyards. Location Temecula california

```html
<!DOCTYPE html>
<html lang="en">
<head>
<meta charset="utf-8">
<title>Corvelle Vineyards – Malbec 2020 Label</title>
<link rel="stylesheet" href="https://fonts.googleapis.com/css2?family=Cinzel:wght@400;500&display=swap">
<style>
  :root {
    --backdrop: #dcd3bf;
    --paper: #f5f2eb;
    --ink: #651a10;
  }
  html, body {
    margin: 0;
    padding: 0;
    width: 1200px;
    height: 909px;
    overflow: hidden;
    background: var(--backdrop);
  }
  .canvas {
    position: relative;
    width: 1200px;
    height: 909px;
  }
  .label {
    position: absolute;
    left: 312px;
    top: 44px;
    width: 577px;
    height: 820px;
    background: var(--paper);
    color: var(--ink);
    font-family: "Cinzel", "Trajan Pro", serif;
    box-sizing: border-box;
  }
  .label-frame {
    position: absolute;
    inset: 14px;
    border: 1.5px solid var(--ink);
  }
  .label-text {
    position: absolute;
    left: 0;
    right: 0;
    margin: 0;
    text-align: center;
    line-height: 1;
    font-weight: 400;
  }
  .brand-name {
    top: 218px;
    font-size: 76px;
    letter-spacing: 0.02em;
  }
  .brand-sub {
    top: 362px;
    font-size: 38px;
    letter-spacing: 0.08em;
  }
  .varietal-rule {
    position: absolute;
    left: 50%;
    width: 216px;
    height: 4px;
    margin-left: -108px;
  }
  .varietal-rule.top { top: 529px; }
  .varietal-rule.bottom { top: 569px; }
  .varietal {
    top: 537px;
    font-size: 26px;
    letter-spacing: 0.04em;
  }
  .vintage {
    top: 586px;
    font-size: 27px;
    letter-spacing: 0.02em;
  }
  .appellation {
    top: 710px;
    font-size: 26px;
    letter-spacing: 0.04em;
  }
</style>
</head>
<body>
<main class="canvas">
  <section class="label" aria-label="Corvelle Vineyards Malbec 2020 wine label">
    <div class="label-frame"></div>

    <h1 class="label-text brand-name">CORVELLE</h1>
    <p class="label-text brand-sub">VINEYARDS</p>

    <svg class="varietal-rule top" viewBox="0 0 216 4" preserveAspectRatio="none" aria-hidden="true">
      <path d="M0 2 Q108 -0.5 216 2 Q108 4.5 0 2 Z" fill="var(--ink)"/>
    </svg>
    <p class="label-text varietal">MALBEC</p>
    <svg class="varietal-rule bottom" viewBox="0 0 216 4" preserveAspectRatio="none" aria-hidden="true">
      <path d="M0 2 Q108 -0.5 216 2 Q108 4.5 0 2 Z" fill="var(--ink)"/>
    </svg>
    <p class="label-text vintage">2020</p>

    <p class="label-text appellation">Temecula Valley, California</p>
  </section>
</main>
</body>
</html>
```